BrXpertz Business Cards for SME Experts

We need a business card for a new company based in Clearwater FL called Kestrel of Merit. KoM is your access to on-demand subject matter experts. The final design should be very clean communicating innovation and expertise. Our logo design is attached.

The Information Age has affected the workforce in that automation and computerization have resulted in higher productivity coupled with net job loss of many knowledgeable employees. Combined with the creation of the internet and search capabilities, the disintermediation of the value chain of Subject Matter Experts (SME) has happened. We no longer need to work through traditional consulting firms for all consulting needs, instead the direct access to the SME, through a leaner and lower cost model is what the market is demanding.
BrXpertz is a new marketplace to buy consulting services. The business model is that all consultants (subject matter experts) can become a consulting resource in the marketplace following our guidelines. The consumer can now easily access consultants that they could not find easily before.
In much the way an Zyla car can be identified and requested, so can a BrXpertz Consultant. Each consultant can be identified by: location, expertise, billing rate, and prior experience rating.
By seamlessly connecting consultants to requesters through a new Kestrel of Merit marketplace, you now will have an easy to use and quicker turnaround to request and staff your consulting needs. Leveraging the KoM app, you can access the subject matter expert you need for your business requirement.

Target Market(s)

Small and medium sized companies; non-profits

Industry/Entity Type

Business Consultant

Contact Information for Business Card

Name
website
email address
Logo
mailing address (debating if I really need...)
twitter
LinkedIn

Requirements
Must have
• the logo I have included in the design; want the colors to be consistent with the logo design

```html
<!DOCTYPE html>
<html lang="en">
<head>
<meta charset="utf-8">
<title>Kestrel of Merit – Business Card</title>
<link href="https://fonts.googleapis.com/css2?family=Ubuntu:wght@500;700&family=Open+Sans:wght@400&display=swap" rel="stylesheet">
<style>
  :root {
    --navy: #1b2466;
    --cyan: #1ea3cf;
    --white: #ffffff;
    --backdrop: #4e4e4e;
    --rule: #9aa0b8;
  }
  html, body {
    margin: 0;
    width: 1105px;
    height: 1200px;
    overflow: hidden;
    background: var(--backdrop);
  }
  .card {
    position: absolute;
    left: 196px;
    width: 720px;
    height: 412px;
    background: var(--white);
    overflow: hidden;
  }
  .card--front { top: 146px; }
  .card--back { top: 602px; }
  .card__bg { position: absolute; inset: 0; }

  .brand {
    position: absolute;
    left: 190px;
    transform: translateX(-50%);
    text-align: center;
    color: var(--navy);
    font-family: "Ubuntu", sans-serif;
    font-weight: 500;
    white-space: nowrap;
  }
  .brand__mark { top: 140px; font-size: 46px; }
  .brand__name { top: 240px; font-size: 30px; }

  .holder {
    position: absolute;
    right: 46px;
    top: 40px;
    text-align: right;
    font-family: "Ubuntu", sans-serif;
  }
  .holder__name { color: var(--cyan); font-size: 23px; font-weight: 500; }
  .holder__role { color: var(--white); font-size: 17px; font-weight: 700; margin-top: 4px; }

  .contact {
    position: absolute;
    right: 46px;
    top: 314px;
    list-style: none;
    margin: 0;
    padding: 0;
    font-family: "Open Sans", sans-serif;
    font-size: 19px;
    color: var(--white);
    text-align: right;
  }
  .contact li { display: flex; align-items: center; justify-content: flex-end; gap: 10px; line-height: 30px; }
  .contact svg { width: 18px; height: 18px; }

  .back-mark {
    position: absolute;
    left: 0; right: 0;
    top: 140px;
    text-align: center;
    font-family: "Ubuntu", sans-serif;
    font-weight: 700;
    font-size: 96px;
    color: var(--navy);
  }
  .social {
    position: absolute;
    left: 101px;
    top: 346px;
    width: 520px;
    height: 32px;
  }
</style>
</head>
<body>

<section class="card card--front" aria-label="Card front">
  <svg class="card__bg" viewBox="0 0 720 412" aria-hidden="true">
    <rect width="720" height="412" fill="var(--navy)"/>
    <circle cx="122" cy="206" r="300" fill="var(--white)"/>
    <circle cx="122" cy="206" r="290" fill="none" stroke="var(--navy)" stroke-width="3"/>
    <path d="M 230 -93 A 320 320 0 0 1 404 206" fill="none" stroke="var(--cyan)" stroke-width="5"/>
    <circle cx="122" cy="206" r="300" fill="none" stroke="var(--white)" stroke-width="4"/>
    <path d="M 218 -78 A 304 304 0 0 1 426 206" fill="none" stroke="var(--cyan)" stroke-width="4"/>
    <circle cx="122" cy="206" r="284" fill="var(--white)"/>
  </svg>

  <div class="brand brand__mark">KoM</div>
  <div class="brand brand__name">Kestrel of Merit</div>

  <div class="holder">
    <div class="holder__name">Dana Whitfield</div>
    <div class="holder__role">Consultant</div>
  </div>

  <ul class="contact">
    <li>Dana@KestrelofMerit.com
      <svg viewBox="0 0 18 18" aria-hidden="true"><rect x="1" y="4" width="16" height="11" fill="var(--cyan)"/><path d="M1 4 L9 11 L17 4" fill="none" stroke="var(--navy)" stroke-width="1.5"/></svg>
    </li>
    <li>www.KestrelofMerit.com
      <svg viewBox="0 0 18 18" aria-hidden="true"><circle cx="9" cy="9" r="8" fill="var(--cyan)"/><ellipse cx="9" cy="9" rx="3.5" ry="8" fill="none" stroke="var(--navy)" stroke-width="1.2"/><line x1="1" y1="9" x2="17" y2="9" stroke="var(--navy)" stroke-width="1.2"/></svg>
    </li>
  </ul>
</section>

<section class="card card--back" aria-label="Card back">
  <div class="back-mark">KoM</div>
  <svg class="social" viewBox="0 0 520 32" aria-label="Social profiles">
    <defs>
      <linearGradient id="rule-left" x1="0" x2="1"><stop offset="0" stop-color="var(--rule)" stop-opacity="0"/><stop offset="1" stop-color="var(--navy)"/></linearGradient>
      <linearGradient id="rule-right" x1="0" x2="1"><stop offset="0" stop-color="var(--navy)"/><stop offset="1" stop-color="var(--rule)" stop-opacity="0"/></linearGradient>
    </defs>
    <rect x="0" y="15" width="215" height="2" fill="url(#rule-left)"/>
    <rect x="305" y="15" width="215" height="2" fill="url(#rule-right)"/>
    <circle cx="242" cy="16" r="16" fill="var(--cyan)"/>
    <circle cx="278" cy="16" r="16" fill="var(--navy)"/>
  </svg>
</section>

</body>
</html>
```